Tax Business Advertisement

Pemberly & Associates Tax Services - Need to develop an advertisement tool suitable for print and electronic advertising. My business provides tax preparation and audit representation for Individuals, Partnerships, Corporations, Estates, Trusts and other entities with tax reporting requirements. I recently had business cards designed by your company, design #8270451 and would need the basic information from the business card on the advertisement.

Some of the following wording may be suitable for the advertisement:

Enrolled Agents are licensed to practice by the IRS. Our services include personal and business tax return preparation, tax audits, offers in compromise, back taxes, forming new business, dissolving business, and much more. We are available to provide services in all 50 states.

Enrolled agents are the only federally licensed tax practitioners who specialize in taxation and who have unlimited rights to represent taxpayers before the IRS.

If you are just starting a business, have been in business for a long time, or just an individual who needs a Tax Professional, Pemberly & Associates Tax Services is the right choice for you.

```html
<!DOCTYPE html>
<html lang="en">
<head>
<meta charset="utf-8">
<title>Pemberly &amp; Associates Tax Services – Advertisement</title>
<link href="https://fonts.googleapis.com/css2?family=Tinos:wght@400;700&display=swap" rel="stylesheet">
<style>
  :root{
    --backdrop:#666666;
    --brand-red:#c0161c;
    --brand-red-dark:#8e0f13;
    --ink-red:#8b1c1c;
    --ink-black:#111111;
    --footer-black:#0c0c0c;
    --paper:#ffffff;
    --photo-warm:#c9a98a;
    --photo-green:#b9bf9d;
    --photo-light:#f3f1ec;
  }
  *{margin:0;padding:0;box-sizing:border-box;}
  html,body{width:1200px;height:1000px;overflow:hidden;}
  body{background:var(--backdrop);font-family:"Tinos","Times New Roman",serif;position:relative;}

  .flyer{position:absolute;left:252px;top:52px;width:695px;height:898px;
    background:linear-gradient(180deg,var(--brand-red) 0%,var(--brand-red-dark) 100%);overflow:hidden;}
  .flyer__shapes{position:absolute;inset:0;}

  .brand{position:absolute;left:205px;top:78px;display:flex;align-items:center;gap:12px;}
  .brand__mark{width:22px;height:22px;background:var(--brand-red);}
  .brand__name{font-size:34px;font-weight:400;color:var(--ink-black);letter-spacing:.2px;}

  .pitch{position:absolute;right:21px;top:176px;width:340px;text-align:right;
    color:var(--ink-red);font-size:16.4px;line-height:22px;}
  .pitch p{margin-bottom:14px;}
  .pitch strong{font-weight:700;}
  .pitch .pitch__big{font-size:18px;}

  .contact{position:absolute;left:18px;top:690px;color:var(--paper);}
  .contact__name{font-size:27px;text-decoration:underline;text-underline-offset:4px;text-decoration-thickness:2px;}
  .contact__role{font-size:17px;margin-top:6px;}
  .contact__address{font-size:17px;line-height:21.5px;margin-top:16px;font-style:normal;}

  .portrait{position:absolute;left:533px;top:656px;width:158px;height:202px;
    background:linear-gradient(180deg,#c44 0%,#7a3a2c 45%,#1d1d1f 100%);}

  .footer{position:absolute;left:0;bottom:0;width:100%;height:40px;background:var(--footer-black);
    color:var(--paper);text-align:center;font-size:18px;font-weight:700;line-height:40px;letter-spacing:.3px;}
</style>
</head>
<body>
  <main class="flyer">
    <svg class="flyer__shapes" width="695" height="898" viewBox="0 0 695 898" aria-hidden="false">
      <defs>
        <linearGradient id="photoTone" x1="0" y1="0" x2="1" y2="0">
          <stop offset="0" stop-color="#c9a98a"/>
          <stop offset="0.28" stop-color="#d8d4c8"/>
          <stop offset="0.5" stop-color="#f3f1ec"/>
          <stop offset="1" stop-color="#fbfaf7"/>
        </linearGradient>
        <linearGradient id="photoShade" x1="0" y1="0" x2="0" y2="1">
          <stop offset="0" stop-color="#ffffff" stop-opacity="0"/>
          <stop offset="0.6" stop-color="#b9bf9d" stop-opacity="0"/>
          <stop offset="1" stop-color="#b9bf9d" stop-opacity=".55"/>
        </linearGradient>
      </defs>
      <g role="img" aria-label="Photo of a hand writing figures with a pen on a ledger sheet beside dollar bills and a calculator">
        <polygon points="0,43 618,43 695,100 695,668 50,668 0,622" fill="url(#photoTone)"/>
        <polygon points="0,43 618,43 695,100 695,668 50,668 0,622" fill="url(#photoShade)"/>
      </g>
      <polyline points="0,46 616,46 695,104" fill="none" stroke="#000" stroke-width="7"/>
      <polyline points="0,620 52,671 695,671" fill="none" stroke="#000" stroke-width="7"/>
    </svg>

    <div class="brand">
      <span class="brand__mark"></span>
      <span class="brand__name">Pemberly &amp; Associates</span>
    </div>

    <section class="pitch">
      <p>Enrolled Agents are licensed to practice by the IRS. Our services include personal and business tax return preparation, tax audits, offers in compromise, back taxes, forming new business, dissolving business, and much more.</p>
      <p>We are available to provide services in<br><strong class="pitch__big">all 50 states.</strong></p>
      <p>Enrolled agents are the only federally licensed tax practitioners who specialize in taxation and who have unlimited rights to represent taxpayers before the IRS</p>
      <p>If you are just starting a business, have been in business for a long time, or just an individual who needs a Tax Professional,</p>
      <p><strong>Pemberly &amp; Associates Tax Services is the</strong><br><strong class="pitch__big">right choice for you.</strong></p>
    </section>

    <section class="contact">
      <h1 class="contact__name">Daniel R Pemberly III, EA, MS</h1>
      <div class="contact__role">Enrolled Agent</div>
      <address class="contact__address">
        4120 Larkspur Avenue, Suite B,<br>
        Fair Oaks, CA 95628<br>
        Phone : (916) 555-0142<br>
        thetaxdesk@example.com
      </address>
    </section>

    <div class="portrait" role="img" aria-label="Portrait photo of the enrolled agent in a dark suit and tie"></div>

    <footer class="footer">www.pemberlytaxhelp.com</footer>
  </main>
</body>
</html>
```